Double-sided business card needed - specific brief

We need a double sided business card designed for our company Radiant Trimline. Having lost a lot of weight myself, the back of the card needs to show my before and after pictures. It needs to cover the entire back side of the card. This might be with my two before pictures over set on top of my main after picture or in separate frames. I'll leave that to your artistic consideration. The front needs to have our logo with contact details centred below.

The cards will be printed by PRINTKO.com and will be rectangular, 84mm x 55mm, but with ROUNDED edges. Please therefore present your designs rectangular but with rounded edges if possible.

The card should be designed in LANDSCAPE orientation.

As well as the logo, the front of the card should have the following details:

Moira Blakewell
Weight Loss Motivator with 189lb personal loss
moira@radiant-trimline.example
+44 (0)7700 900418

The website is important so should perhaps be more bold than the rest:
www.radiant-trimline.example

My brand colours are: Pink #CD2366, Light Pink #FD88AD. Blue #1C9CB1, Light Blue #64C4DE

Target Market(s)

Women 30+

Contact Information for Business Card

As description above

Font styles to use
Sans Serif

Requirements
Must have
• Double sided.
• Back side entirely covered with my before and after pictures.
• You may wish to float my before pictures on top of my after picture or add them in different frames. I look forward to seeing your different suggestions.

```html
<!DOCTYPE html>
<html lang="en">
<head>
<meta charset="utf-8">
<title>Radiant Trimline – Business Card</title>
<link href="https://fonts.googleapis.com/css2?family=Lato:wght@300;400;700;900&display=swap" rel="stylesheet">
<style>
  :root {
    --stage: #b3b1b2;
    --card: #f4f0ef;
    --pink: #cd2366;
    --light-pink: #fd88ad;
    --blue: #1c9cb1;
    --light-blue: #64c4de;
    --ink: #333333;
    --muted: #555555;
    --label: #f4f2f2;
    --white: #ffffff;
  }
  * { box-sizing: border-box; margin: 0; padding: 0; }
  html, body {
    width: 1200px; height: 1200px; overflow: hidden;
    background: var(--stage);
    font-family: "Lato", sans-serif;
  }
  .stage { position: relative; width: 1200px; height: 1200px; }

  .side-label {
    position: absolute;
    font-size: 23px; font-weight: 400; color: var(--label);
    letter-spacing: 0.3px;
  }
  .side-label--front { left: 90px; top: 42px; }
  .side-label--back { left: 204px; top: 590px; }

  .card {
    position: absolute;
    border-radius: 40px;
    overflow: hidden;
    box-shadow: 0 6px 10px rgba(0,0,0,0.28);
  }

  /* Front */
  .card--front {
    left: 76px; top: 91px; width: 782px; height: 447px;
    background: var(--card);
  }
  .brand {
    position: absolute; left: 40px; top: 180px; width: 276px;
    text-align: center; color: var(--pink);
    font-weight: 400; font-size: 34px; line-height: 1.1;
    letter-spacing: 0.5px; text-transform: uppercase;
  }
  .divider {
    position: absolute; left: 371px; top: 91px; width: 3px; height: 263px;
    background: linear-gradient(to bottom, var(--pink) 0 52%, var(--light-blue) 52% 100%);
  }
  .details { position: absolute; left: 432px; top: 134px; width: 330px; }
  .details__name {
    font-size: 32px; font-weight: 900; color: var(--pink);
    letter-spacing: -0.3px; line-height: 1; white-space: nowrap;
  }
  .details__role {
    margin-top: 14px; font-size: 13.5px; font-weight: 400; color: var(--muted);
    white-space: nowrap;
  }
  .contact { list-style: none; margin-top: 22px; }
  .contact__item {
    display: flex; align-items: center; gap: 10px;
    font-size: 15.5px; font-weight: 400; color: var(--ink);
    height: 20px; margin-bottom: 14px; white-space: nowrap;
  }
  .contact__item--web { font-weight: 700; }
  .contact__icon { width: 14px; height: 14px; flex: none; }

  /* Back */
  .card--back {
    left: 223px; top: 645px; width: 840px; height: 480px;
    background: var(--white);
  }
  .photo { position: absolute; top: 0; height: 480px; }
  .photo--before {
    left: 0; width: 419px;
    background: linear-gradient(180deg, #3f5a32 0%, #8f9466 18%, #b9ad80 28%, #e8e6e2 55%, #eeeceb 75%, #5f8a3e 100%);
  }
  .photo--after {
    left: 427px; width: 413px;
    background: linear-gradient(180deg, #d9d3c8 0%, #c9b58e 30%, #2a2f52 58%, #28325a 80%, #3b2a2a 100%);
  }
  .tag {
    position: absolute; top: 406px; width: 142px; height: 37px;
    border-radius: 19px; background: var(--pink); color: var(--white);
    font-size: 17px; font-weight: 400; text-transform: uppercase;
    display: flex; align-items: center; justify-content: center;
  }
  .tag--before { left: 149px; }
  .tag--after { left: 562px; }
</style>
</head>
<body>
<main class="stage">
  <p class="side-label side-label--front">FRONT SIDE</p>

  <section class="card card--front">
    <div class="brand">Radiant<br>Trimline</div>
    <div class="divider"></div>
    <div class="details">
      <h1 class="details__name">MOIRA BLAKEWELL</h1>
      <p class="details__role">Weight Loss Motivator with 189lb personal loss</p>
      <ul class="contact">
        <li class="contact__item">
          <svg class="contact__icon" viewBox="0 0 24 24"><path fill="#1c9cb1" d="M6.6 10.8a15.1 15.1 0 0 0 6.6 6.6l2.2-2.2c.3-.3.7-.4 1-.2 1.1.4 2.3.6 3.6.6.6 0 1 .4 1 1V20c0 .6-.4 1-1 1A17 17 0 0 1 3 4c0-.6.4-1 1-1h3.5c.6 0 1 .4 1 1 0 1.3.2 2.5.6 3.6.1.3 0 .7-.2 1z"/></svg>
          +44 (0)7700 900418
        </li>
        <li class="contact__item">
          <svg class="contact__icon" viewBox="0 0 24 24"><rect x="2" y="5" width="20" height="14" rx="1.5" fill="#64c4de"/><path d="M2.5 6l9.5 7 9.5-7" fill="none" stroke="#f4f0ef" stroke-width="1.6"/></svg>
          moira@radiant-trimline.example
        </li>
        <li class="contact__item contact__item--web">
          <svg class="contact__icon" viewBox="0 0 24 24" fill="none" stroke="#64c4de" stroke-width="1.6"><circle cx="12" cy="12" r="9.5"/><ellipse cx="12" cy="12" rx="4.2" ry="9.5"/><path d="M2.5 12h19M4 7h16M4 17h16"/></svg>
          www.radiant-trimline.example
        </li>
      </ul>
    </div>
  </section>

  <p class="side-label side-label--back">BACK SIDE</p>

  <section class="card card--back">
    <div class="photo photo--before" role="img" aria-label="Before photo: Moira outdoors in a garden holding her cat"></div>
    <div class="photo photo--after" role="img" aria-label="After photo: Moira seated on a leather sofa in a navy jumper"></div>
    <span class="tag tag--before">Before</span>
    <span class="tag tag--after">After</span>
  </section>
</main>
</body>
</html>
```